Quenderix (www.quenderix-demo.net) needs exciting professional PowerPoint pitch template

Quenderix is an exciting new start-up targeting innovative ways to engage with retail customers at the point of sale.

Our customers are looking for us to help them increase the "wallet share" of their retail customers. The retail customer has their wallet open at the Point of Sale and are paying money to our customer. At Quenderix we are all about attracting the attention of the retail customer AT THAT POINT IN TIME and engaging the retail customer in spending a little more in that store or another store that has a relationship to the retail customer's purchase.

Our customers are the owners of very large supermarkets, chain stores, and financial institutions, and therefore when we pitch a proposal to these buyers it needs to be slick, professional, and very memorable.

The PowerPoint sales presentation template is a key part of striking that impression.

Here is some background...

Our Vision
Through applying new thinking to a mature industry we are reinventing selected segments of the Australian retail messaging business, generating significant value for our customers, our suppliers, and our owners.
We operate with integrity, agility, and intelligence to doing things smarter, faster and more efficiently.
We bring deep industry expertise, deep relationships with customers and suppliers, and a will to see the old ways give way to smarter ways – this is why we win.
From this economically sustainable platform, we will examine the disruption of other market segments by further leveraging the elements that make us successful.

Our Values
With our clients, with our suppliers, with our staff, and with our owners:
# We Partner – We align the interest of all stakeholders by striving to ensure everything we do is mutually beneficial and commercially sustainable in the long term. We are clear with all our stakeholders about what our expectations are of them, and we seek clarity from them in their expectations of us.
# We Innovate – In the segments we choose to compete in, we bring fresh ideas, new business processes, the right relationships, and the right technology to ensure the supply chain is nimble, competitive, and reliable.
# We are Accountable – We say what we will do, and then do what we say.
# We Perform – We use our skills, relationships, and reputation to deliver value to our customers, suppliers, and owners.

Initially we are building our business from low-tech through printing promotional offers and retailer messages on ATM and EFTPOS receipts, but as soon as cash flow supports it we will be engaging in high-tech real-time targeted offers to the specific consumer through video wall offers as people are at the checkout or walking through the shopping centre.

I'd like the PowerPoint template to reflect our vision and values.

The PowerPoint template will be used in communicating our proposals to our clients, and needs to catch and hold our audiences attention.

Please check out the web site we have just launched - it is pretty basic but it has only been up a week. We intend to sharpen it over the coming weeks, but you'll get the idea of what our core messages are.

I have recently sourced a logo from Sketchloft, plus business cards, and have attached the source files for your reference.
Updates

Hi everybody.  Thanks for the designs submitted so far.  Your submissions have helped me understand what I do and don't prefer, and I have updated the "Must Have/Nice to Have/Shouldn't Have" criteria accordingly.  I have also uploaded a powerpoint template that I had at a company I udsed to run that has the sort of visual theme I find appealing. I have more time to provide feedback now that the week is over, so I will comment on individual designs shortly, and I will respond to queries directed to me.

Kind Regards - Gareth

Target Market(s)

Our customers are large corporations that have professional Point Of Sale marketing experts looking for a supplier with an edge over others in a crowded market. The buyer of our product and services is ultimately a communications expert. They want to see distinctive competence, and an agility of thinking that will make them money through driving more consumer spending.

Industry/Entity Type

Financial

Font styles to use
Sans Serif

Colors
34a7d7
0892cd
3276b5

Requirements
Must have
• The following Slides: Title Slide, Agenda, About Quenderix, Thank you
The pages must be easy on the eye.
The final product must be a PowerPoint template file with the usual "Title", "Title and Content", "Title & Table", and "Blank" page types.
Widescreen format please.
Nice to have
• The pages should have an eye-catching visual element running through all the pages. I have attached a template from a company i used to be involved with that has a visual theme running through it that I like.
Plenty of whitespace - have a look at www.quenderix-demo.net.
Bonus points for pulling the text from the brief into the template.
Use "Innovation - Integrity - Service" as the tag line.
Should not have
• Pages should not be busy.
Stay away from too much black. I know the cards have black, but the presentation shouldn't.
I dont like serifed fonts. Use Blenvotz's Fjord Kit style for insporation.
The "Keeping Vivid" tag line was an invention of the logo designer that we do not want to cary forward. Please do not use it.

```html
<!DOCTYPE html>
<html lang="en">
<head>
<meta charset="utf-8">
<title>Quenderix Presentation Template</title>
<link href="https://fonts.googleapis.com/css2?family=Open+Sans:wght@400;600;700&display=swap" rel="stylesheet">
<style>
  :root {
    --navy: #0f2c55;
    --brand: #0892cd;
    --sky: #34a7d7;
    --steel: #3276b5;
    --bar: #0a78c8;
    --grey-box: #9ea3a8;
    --text: #6f7479;
    --text-dark: #4b5056;
    --row-a: #dde8f4;
    --row-b: #c8d9ee;
    --page: #ffffff;
  }
  * { box-sizing: border-box; margin: 0; padding: 0; }
  html, body { width: 1200px; height: 900px; overflow: hidden; background: var(--page); }
  body { position: relative; font-family: "Open Sans", Arial, sans-serif; }

  .slide {
    position: absolute; width: 377px; height: 285px; background: #fff;
    box-shadow: 1px 2px 5px rgba(0,0,0,.35); overflow: hidden;
  }
  .col-1 { left: 16px; } .col-2 { left: 406px; } .col-3 { left: 799px; }
  .row-1 { top: 10px; } .row-2 { top: 308px; } .row-3 { top: 605px; }

  /* cover slides */
  .cover-art {
    position: absolute; left: 0; top: 0; width: 377px; height: 215px;
    background:
      radial-gradient(ellipse 180px 120px at 180px 60px, rgba(120,180,225,.55), transparent 70%),
      linear-gradient(160deg, #3c7fb8 0%, #1e5a97 45%, #12396e 100%);
  }
  .cover-wordmark { position: absolute; left: 10px; top: 190px; color: #fff; font-size: 13px; font-weight: 700; }
  .cover-title { position: absolute; left: 10px; top: 231px; font-size: 16px; font-weight: 400; color: var(--brand); }
  .cover-sub { position: absolute; left: 10px; top: 263px; font-size: 10px; color: var(--text); }

  .wordmark-small { position: absolute; right: 9px; bottom: 11px; color: var(--steel); font-size: 8px; font-weight: 700; }

  /* content slides */
  .slide-head {
    position: absolute; left: 0; top: 0; width: 100%; height: 38px;
    background:
      linear-gradient(115deg, transparent 62%, rgba(255,255,255,.12) 64%, transparent 72%),
      linear-gradient(90deg, #1c5a96 0%, #184b84 55%, #0f2c55 100%);
    color: #fff; font-size: 15.5px; font-weight: 400; padding: 8px 0 0 12px;
  }
  .slide-foot {
    position: absolute; left: 0; bottom: 0; width: 100%; height: 7px; background: var(--bar);
    color: #fff; font-size: 4.5px; display: flex; justify-content: space-between; align-items: center;
    padding: 0 8px;
  }
  .slide-foot .tag { position: absolute; left: 50%; transform: translateX(-50%); }

  .agenda { position: absolute; left: 9px; top: 58px; list-style: none; }
  .agenda li { display: flex; align-items: center; height: 24px; margin-bottom: 10.3px; }
  .agenda .num {
    width: 20px; height: 22px; background: var(--grey-box); color: #fff; font-size: 12px;
    font-weight: 700; display: flex; align-items: center; justify-content: center;
    border: 1px solid #c4c7ca;
  }
  .agenda .item {
    margin-left: 11px; width: 322px; height: 24px; background: var(--bar); color: #fff;
    font-size: 8.2px; line-height: 10px; padding: 1px 4px 0 4px;
  }
  .agenda .item span { display: block; width: 300px; }

  .body { position: absolute; left: 13px; right: 18px; color: var(--text); font-size: 10px; line-height: 12px; }
  .kicker { color: var(--steel); font-weight: 700; font-size: 10px; }
  .bullets { list-style: none; }
  .bullets > li { position: relative; padding-left: 14px; margin-bottom: 6px; }
  .bullets > li::before { content: "•"; position: absolute; left: 1px; color: var(--brand); }
  .dashes { list-style: none; margin-top: 7px; }
  .dashes li { position: relative; padding-left: 17px; margin-bottom: 6px; font-size: 9.3px; line-height: 12px; }
  .dashes li::before { content: "–"; position: absolute; left: 3px; color: var(--steel); }
  .accent { color: var(--brand); }

  .center-title { position: absolute; left: 0; width: 100%; top: 46px; text-align: center; color: var(--brand); font-size: 11px; font-weight: 400; }

  .data-table { position: absolute; left: 60px; top: 126px; border-collapse: collapse; font-size: 7.8px; }
  .data-table th { background: var(--bar); color: #fff; font-weight: 700; height: 15px; padding: 0 4px; border: 1px solid #fff; }
  .data-table td { text-align: center; color: var(--text-dark); height: 15px; width: 54px; border: 1px solid #fff; }
  .data-table tr:nth-child(odd) td { background: var(--row-a); }
  .data-table tr:nth-child(even) td { background: var(--row-b); }

  .chart-frame { position: absolute; left: 76px; top: 112px; width: 205px; height: 154px; border: 1px dashed var(--sky); }
  .chart { position: absolute; left: 0; top: 0; }
</style>
</head>
<body>

<!-- Title -->
<section class="slide col-1 row-1">
  <div class="cover-art" role="img" aria-label="Blue world map artwork with soft light streaks"></div>
  <div class="cover-wordmark">Quenderix</div>
  <h1 class="cover-title">Presentation title</h1>
  <p class="cover-sub">Presentation subtitle</p>
</section>

<!-- Agenda -->
<section class="slide col-2 row-1">
  <h2 class="slide-head">Agenda Slide</h2>
  <ol class="agenda">
    <li><span class="num">1</span><span class="item"><span>Lorem ipsum dolor sit amet, consectetur adipiscing elit. Cras vitae tincidunt felis.</span></span></li>
    <li><span class="num">2</span><span class="item"><span>Lorem ipsum dolor sit amet, consectetur adipiscing elit. Cras vitae tincidunt felis.</span></span></li>
    <li><span class="num">3</span><span class="item"><span>Lorem ipsum dolor sit amet, consectetur adipiscing elit. Cras vitae tincidunt felis.</span></span></li>
    <li><span class="num">4</span><span class="item"><span>Lorem ipsum dolor sit amet, consectetur adipiscing elit. Cras vitae tincidunt felis.</span></span></li>
    <li><span class="num">5</span><span class="item"><span>Lorem ipsum dolor sit amet, consectetur adipiscing elit. Cras vitae tincidunt felis.</span></span></li>
    <li><span class="num">6</span><span class="item"><span>Lorem ipsum dolor sit amet, consectetur adipiscing elit. Cras vitae tincidunt felis.</span></span></li>
  </ol>
  <div class="wordmark-small">Quenderix</div>
  <footer class="slide-foot"><span>16-11-2013</span><span class="tag">Innovation - Integrity - Service</span><span>2</span></footer>
</section>

<!-- About: Vision -->
<section class="slide col-3 row-1">
  <h2 class="slide-head">About Quenderix</h2>
  <div class="body" style="top:49px; right:14px">
    <p class="kicker" style="margin-bottom:19px">Our Vision</p>
    <ul class="bullets">
      <li>Through applying new thinking to a mature industry we are reinventing selected segments of the Australian retail messaging business, generating significant value for our customers, our suppliers, and our owners.</li>
      <li>We operate with integrity, agility, and intelligence to doing things smarter, faster and more efficiently.<br>We bring deep industry expertise, deep relationships with customers and suppliers, and a will to see the old ways give way to smarter ways – this is why we win.</li>
      <li>From this economically sustainable platform, we will examine the disruption of other market segments by further leveraging the elements that make us successful.</li>
    </ul>
  </div>
  <div class="wordmark-small">Quenderix</div>
  <footer class="slide-foot"><span>16-11-2013</span><span class="tag">Innovation - Integrity - Service</span><span>3</span></footer>
</section>

<!-- About: Values -->
<section class="slide col-1 row-2">
  <h2 class="slide-head">About Quenderix</h2>
  <div class="body" style="top:47px; right:28px">
    <ul class="bullets">
      <li><span class="kicker">Our Values</span><br>With our clients, with our suppliers, with our staff, and with our owners:
        <ul class="dashes">
          <li><span class="accent">We Partner</span> – We align the interest of all stakeholders by striving to ensure everything we do is mutually beneficial and commercially sustainable in the long term. We are clear with all our stakeholders about what our expectations are of them, and we seek clarity from them in their expectations of us.</li>
          <li><span class="accent">We Innovate</span> – In the segments we choose to compete in, we bring fresh ideas, new business processes, the right relationships, and the right technology to ensure the supply chain is nimble, competitive, and reliable.</li>
          <li><span class="accent">We are Accountable</span> – We say what we will do, and then do what we say.</li>
          <li><span class="accent">We Perform</span> – We use our skills, relationships, and reputation to deliver value to our customers, suppliers, and owners.</li>
        </ul>
      </li>
    </ul>
  </div>
  <div class="wordmark-small">Quenderix</div>
  <footer class="slide-foot"><span>16-11-2013</span><span class="tag">Innovation - Integrity - Service</span><span>4</span></footer>
</section>

<!-- Text and Table -->
<section class="slide col-2 row-2">
  <h2 class="slide-head">Text and Table</h2>
  <h3 class="center-title">Table Title</h3>
  <div class="body" style="top:66px">
    <ul class="bullets"><li>Lorem ipsum dolor sit amet, consectetur adipiscing elit. Cras vitae tincidunt felis. Vestibulum eget risus nec justo consequat tincidunt eget non tellus. Donec in orci eu turpis condimentum ultricies.</li></ul>
  </div>
  <table class="data-table">
    <thead><tr><th>Category A</th><th>Category B</th><th>Category C</th><th>Category D</th><th>Category E</th></tr></thead>
    <tbody>
      <tr><td>111.222</td><td>666.555</td><td>999.222</td><td>111.222</td><td>666.555</td></tr>
      <tr><td>222.333</td><td>777.666</td><td>333.666</td><td>222.333</td><td>777.666</td></tr>
      <tr><td>333.444</td><td>888.999</td><td>111.444</td><td>333.444</td><td>888.999</td></tr>
      <tr><td>444.555</td><td>555.333</td><td>888.666</td><td>444.555</td><td>555.333</td></tr>
      <tr><td>555.666</td><td>444.555</td><td>555.222</td><td>555.666</td><td>444.555</td></tr>
    </tbody>
  </table>
  <div class="wordmark-small">Quenderix</div>
  <footer class="slide-foot"><span>16-11-2013</span><span class="tag">Innovation - Integrity - Service</span><span>5</span></footer>
</section>

<!-- Text and Graphic -->
<section class="slide col-3 row-2">
  <h2 class="slide-head">Text and Graphic slide</h2>
  <h3 class="center-title">Graphic Title</h3>
  <div class="body" style="top:66px">
    <ul class="bullets"><li>Lorem ipsum dolor sit amet, consectetur adipiscing elit. Cras vitae tincidunt felis. Vestibulum eget risus nec justo consequat tincidunt eget non tellus. Donec in orci eu turpis condimentum ultricies.</li></ul>
  </div>
  <div class="chart-frame"></div>
  <svg class="chart" width="377" height="285" viewBox="0 0 377 285" aria-label="Donut chart">
    <g transform="rotate(-90 181 189)" fill="none" stroke-width="42">
      <circle cx="181" cy="189" r="56" stroke="#0277c8" stroke-dasharray="206.09 351.86" stroke-dashoffset="0"/>
      <circle cx="181" cy="189" r="56" stroke="#1aa6e0" stroke-dasharray="80.43 351.86" stroke-dashoffset="-206.09"/>
      <circle cx="181" cy="189" r="56" stroke="#12365f" stroke-dasharray="35.19 351.86" stroke-dashoffset="-286.52"/>
      <circle cx="181" cy="189" r="56" stroke="#9aa3ac" stroke-dasharray="30.16 351.86" stroke-dashoffset="-321.71"/>
    </g>
    <g fill="#fff" font-family="Open Sans, Arial, sans-serif" font-size="9" text-anchor="middle">
      <text x="241" y="205">8,2</text>
      <text x="141" y="207">3,2</text>
      <text x="149" y="158">1,4</text>
      <text x="175" y="140">1,2</text>
    </g>
  </svg>
  <div class="wordmark-small">Quenderix</div>
  <footer class="slide-foot"><span>16-11-2013</span><span class="tag">Innovation - Integrity - Service</span><span>6</span></footer>
</section>

<!-- Thank you -->
<section class="slide col-1 row-3">
  <div class="cover-art" role="img" aria-label="Blue world map artwork with soft light streaks"></div>
  <div class="cover-wordmark">Quenderix</div>
  <h2 class="cover-title">THANK YOU</h2>
  <p class="cover-sub">FOR YOUR TIME</p>
</section>

</body>
</html>
```